Aged Care Home - TM

We need a website design for a homepage and a content page for an aged care home in Brisbane. I have attached a detailed design/content brief and their logo to be used in concepts. Also bear in mind this design will be skinned for Dot Net Nuke 4.8.2 so design needs to be used on this content management system.

The following elements are required in the design:

• Phone number will be featured in banner on each page 07 5281 6637

• An area for a large flash banner of rotating images on homepage

• Images need to reflect credibility, professionalism and caring (just use some example images for now as we’ll need to source some)

• Large logo in banner as well

• Some icons on homepage to include:

• Download Application Form

• Admission Kit

• Contact Us

```html
<!DOCTYPE html>
<html lang="en">
<head>
<meta charset="utf-8">
<title>The TM Home – Aged Care</title>
<link rel="stylesheet" href="https://fonts.googleapis.com/css2?family=Cabin:wght@400;500&family=PT+Sans:wght@400;700&display=swap">
<style>
:root{
  --navy:#1c1a73;
  --sky:#8cc4f2;
  --band-top:#8ec3f5;
  --band-bottom:#1577ef;
  --panel:#e0e0e0;
  --panel-line:#a9a9a9;
  --card-line:#b7b7b7;
  --body-text:#222;
  --muted:#9a9a9a;
  --more:#e8151d;
  --green:#5cc12c;
  --green-dark:#3d9a16;
  --white:#fff;
}
*{margin:0;padding:0;box-sizing:border-box}
html,body{width:1200px;height:938px;overflow:hidden;background:var(--white)}
body{position:relative;font-family:"PT Sans",Tahoma,sans-serif;color:var(--body-text)}

.brand{position:absolute;left:100px;top:52px;display:flex;align-items:center;gap:16px;font-family:"Cabin",sans-serif;font-weight:400;color:var(--navy)}
.brand-mark{width:26px;height:26px;background:var(--navy);border-radius:50%}
.brand-name{font-size:42px;letter-spacing:1px;line-height:1}
.brand-name small{font-size:22px;display:block;margin-bottom:2px}

.welcome{position:absolute;right:34px;top:193px;font-size:17px;letter-spacing:2.6px;color:var(--sky)}

.hero-band{position:absolute;left:0;top:230px;width:1200px;height:281px;background:linear-gradient(180deg,var(--band-top),var(--band-bottom))}
.hero-art{position:absolute;left:0;top:0;width:363px;height:281px;background:linear-gradient(135deg,#bcd9f4 0%,#5a9fe6 55%,#8a7350 100%)}
.banner{position:absolute;left:328px;top:25px;width:852px;height:141px;background:var(--white);border-radius:10px}
.banner-photo{position:absolute;left:9px;top:9px;width:826px;height:125px;border-radius:4px;background:linear-gradient(180deg,#5d86b8 0%,#c9d8ea 45%,#e9eef4 70%,#6e9a3c 100%)}
.banner-name{position:absolute;right:36px;top:22px;font-family:"Cabin",sans-serif;font-size:31px;color:var(--navy);letter-spacing:.5px}
.banner-phone{position:absolute;right:27px;top:64px;font-family:"Cabin",sans-serif;font-size:21px;color:var(--navy);letter-spacing:3px}

.main-nav{position:absolute;right:28px;top:248px;display:flex;align-items:center;font-size:16px;color:var(--white)}
.main-nav a{color:var(--white);text-decoration:none}
.main-nav a.current{font-weight:700}
.main-nav .sep{width:2px;height:14px;background:var(--green);margin:0 16px}

.intro{position:absolute;left:18px;top:526px;width:280px;height:310px;background:var(--panel);border:1px solid var(--panel-line);border-radius:8px;padding:16px 12px 0 14px}
.intro-photo{width:250px;height:93px;background:linear-gradient(180deg,#a04a3a,#8a2f2a 50%,#4f6a3a);margin-bottom:10px}
.intro p{font-size:12.5px;line-height:14.4px;margin-bottom:14px;white-space:nowrap}

.feature{position:absolute;left:309px;top:554px;width:372px;height:255px;border:1px solid var(--card-line);border-radius:8px;overflow:hidden;background:linear-gradient(160deg,#eef0f5 0%,#c6ccd8 55%,#9aa3b7 100%)}
.feature-title{position:absolute;left:24px;top:30px;font-family:"Cabin",sans-serif;font-size:33px;color:var(--navy)}

.card{position:absolute;width:243px;height:124px;border:1px solid var(--card-line);border-radius:8px;background:var(--white)}
.card-icon{position:absolute;left:9px;top:11px;width:37px;height:37px}
.card-photo{position:absolute;left:53px;top:5px;width:183px;height:51px;border-radius:6px}
.card p{position:absolute;left:9px;top:59px;font-size:11.5px;line-height:14px;letter-spacing:.2px;color:var(--muted);white-space:nowrap}
.card .more{position:absolute;left:132px;top:101px;font-size:11.5px;line-height:14px;font-weight:700;color:var(--more);text-decoration:none}
.c1{left:691px;top:554px}.c2{left:940px;top:554px}.c3{left:691px;top:684px}.c4{left:940px;top:684px}

.site-footer{position:absolute;left:0;top:853px;width:1200px;height:85px;background:linear-gradient(180deg,#f6fafe,#cfe4fb)}
.copyright{position:absolute;left:0;width:1200px;top:20px;text-align:center;font-size:12px;letter-spacing:.8px;color:var(--muted)}
.counter{position:absolute;right:34px;top:31px;font-size:12px;letter-spacing:1px;color:var(--sky)}
</style>
</head>
<body>

<header>
  <div class="brand"><span class="brand-mark"></span><span class="brand-name"><small>the</small>TM HOME</span></div>
  <div class="welcome">Welcome to The TM Home - On Line</div>
</header>

<section class="hero-band">
  <div class="hero-art" role="img" aria-label="Hand placing a puzzle piece over a cottage on a sky-blue jigsaw"></div>
  <div class="banner">
    <div class="banner-photo" role="img" aria-label="Couple standing on a grassy hill beside a faint house outline under a blue sky"></div>
    <div class="banner-name">TM HOME</div>
    <div class="banner-phone">07 5281 6637</div>
  </div>
  <nav class="main-nav">
    <a class="current" href="#">Home</a><span class="sep"></span>
    <a href="#">About</a><span class="sep"></span>
    <a href="#">Accomedation Option</a><span class="sep"></span>
    <a href="#">Contact Us</a><span class="sep"></span>
    <a href="#">Brochurs &amp; Forms</a>
  </nav>
</section>

<aside class="intro">
  <div class="intro-photo" role="img" aria-label="Brick entrance sign of the home"></div>
  <p>We are an Aged Care Facility that has been<br>providing quality care and accommodation<br>to the Brisbane community for over twenty<br>years.</p>
  <p>From this site you can learn more about us,<br>find out all the types of accommodation<br>available, what our Philosophy of Care is,<br>send a message to a resident, contact us to<br>request more information or download a<br>brochure or an application form.</p>
</aside>

<section class="feature" role="img" aria-label="Bright bedroom with armchairs, lamps and a made bed">
  <div class="feature-title">TM HOME</div>
</section>

<article class="card c1">
  <svg class="card-icon" viewBox="0 0 37 37"><circle cx="18.5" cy="18.5" r="17" fill="var(--green)" stroke="var(--green-dark)"/><circle cx="18.5" cy="14" r="5" fill="#fff"/><path d="M10 28c1-6 5-8 8.5-8s7.5 2 8.5 8z" fill="#fff"/></svg>
  <div class="card-photo" role="img" aria-label="Warm-lit bedroom with a red bedspread" style="background:linear-gradient(90deg,#d06a14,#f0a040 60%,#c43a1c)"></div>
  <p>We have range of accommodation<br>styles to suit a wide variety of needs.<br>The following types of accommodation<br>are offered</p>
  <a class="more" href="#">MORE »</a>
</article>

<article class="card c2">
  <svg class="card-icon" viewBox="0 0 37 37"><circle cx="18.5" cy="18.5" r="17" fill="var(--green)" stroke="var(--green-dark)"/><rect x="11" y="17" width="4" height="10" fill="#fff"/><rect x="17" y="11" width="4" height="16" fill="#fff"/><rect x="23" y="14" width="4" height="13" fill="#fff"/></svg>
  <div class="card-photo" role="img" aria-label="Couple silhouetted against a sunset" style="background:linear-gradient(180deg,#f3b23a,#e0621a 55%,#3a1c14)"></div>
  <p>We have range of accommodation<br>styles to suit a wide variety of needs.<br>The following types of accommodation<br>are offered</p>
  <a class="more" href="#">MORE »</a>
</article>

<article class="card c3">
  <svg class="card-icon" viewBox="0 0 37 37"><circle cx="18.5" cy="18.5" r="17" fill="var(--green)" stroke="var(--green-dark)"/><rect x="12" y="9" width="13" height="19" rx="1" fill="#fff"/><path d="M15 14h7M15 18h7M15 22h7" stroke="var(--green)" stroke-width="1.5"/></svg>
  <div class="card-photo" role="img" aria-label="Fountain pen resting on printed charts" style="background:linear-gradient(90deg,#e8ecf2,#b9c6d6 60%,#d7b98a)"></div>
  <p>We have range of accommodation<br>styles to suit a wide variety of needs.<br>The following types of accommodation<br>are offered</p>
  <a class="more" href="#">MORE »</a>
</article>

<article class="card c4">
  <svg class="card-icon" viewBox="0 0 37 37"><circle cx="18.5" cy="18.5" r="17" fill="var(--green)" stroke="var(--green-dark)"/><path d="M18.5 9v11M13.5 15l5 5 5-5" stroke="#fff" stroke-width="2.5" fill="none"/><path d="M11 23v4h15v-4" stroke="#fff" stroke-width="2.5" fill="none"/></svg>
  <div class="card-photo" role="img" aria-label="Person by a mailbox in the snow" style="background:linear-gradient(90deg,#eceff3,#c9ced6 50%,#8e9aa8)"></div>
  <p>We have range of accommodation<br>styles to suit a wide variety of needs.<br>The following types of accommodation<br>are offered</p>
  <a class="more" href="#">MORE »</a>
</article>

<footer class="site-footer">
  <div class="copyright">Copyright © 2008 AgedCare TM Home, Tel 07 5281 6637</div>
  <div class="counter">01067</div>
</footer>

</body>
</html>
```